Brenmoor Estates Website and Logo Design

We need a new logo and website designed for 'Brenmoor Estates Ltd', which is a well established Guernsey property holding company founded in 1934.

The company does not currently have a website. The new website should be similar in style and layout to https://www.quillfenhouse.example/.

Target Market(s)

Industry, Media, Tenants

Industry/Entity Type

Property Management

Logo Text

BEL OR Brenmoor Estates Ltd OR BE

Coding

Coded - Design and coding required

Number of Pages Required

4 page

Font styles to use
Other font styles liked:
• Helvetica

Requirements
Must have
• The logo laying over the picture (like https://www.quillfenhouse.example/).
• Big pictures on homepage (like https://www.quillfenhouse.example/)

```html
<!DOCTYPE html>
<html lang="en">
<head>
<meta charset="utf-8">
<title>Brenmoor Estates Ltd</title>
<link href="https://fonts.googleapis.com/css2?family=Cabin:wght@400;500;600&family=Lato:wght@300;400;700&display=swap" rel="stylesheet">
<style>
:root{
  --blue:#2f5ea8;
  --link:#2b5aa6;
  --ink:#1d1d1d;
  --text:#333333;
  --bg:#fafafa;
  --white:#ffffff;
  --footer:#353535;
  --footer-deep:#262626;
  --muted:#8a8a8a;
}
*{box-sizing:border-box;margin:0;padding:0}
html,body{width:1200px;height:3352px;overflow:hidden}
body{background:var(--bg);font-family:"Lato",Helvetica,sans-serif;color:var(--text);position:relative}
section,header,footer{position:absolute;left:0;width:1200px}
.heading{font-family:"Cabin",Helvetica,sans-serif}

/* Hero */
.hero{top:0;height:588px;background:linear-gradient(180deg,#7d8fb4 0%,#a3adc0 18%,#c9c5bd 32%,#a49d93 52%,#6f7780 66%,#4b5e72 80%,#34495e 100%)}
.brand{position:absolute;left:26px;top:10px;display:flex;align-items:center;gap:14px}
.brand-mark{width:80px;height:80px;border-radius:50%;border:3px solid var(--white)}
.brand-name{font-family:"Cabin",Helvetica,sans-serif;font-weight:500;font-size:24px;letter-spacing:2px;color:var(--white);padding-left:14px;border-left:2px solid var(--white);line-height:50px}
.main-nav{position:absolute;top:36px;left:536px;display:flex;gap:27px;font-family:"Cabin",Helvetica,sans-serif;font-weight:600;font-size:19px;color:var(--white)}
.cta{position:absolute;left:999px;top:29px;width:167px;height:43px;border:3px solid var(--white);border-radius:5px;color:var(--white);font-family:"Cabin",Helvetica,sans-serif;font-weight:600;font-size:19px;text-align:center;line-height:37px}
.hero-kicker{position:absolute;top:264px;width:100%;text-align:center;color:var(--white);font-family:"Cabin",Helvetica,sans-serif;font-size:26px;text-shadow:0 1px 4px rgba(0,0,0,.5)}
.hero-title{position:absolute;top:302px;width:100%;text-align:center;color:var(--white);font-family:"Cabin",Helvetica,sans-serif;font-weight:600;font-size:41px;text-shadow:0 1px 5px rgba(0,0,0,.5)}
.btn{position:absolute;background:var(--blue);color:var(--white);font-family:"Cabin",Helvetica,sans-serif;font-weight:500;font-size:20px;text-align:center;border-radius:3px}
.hero .btn{left:509px;top:375px;width:168px;height:50px;line-height:50px}
.arrow{position:absolute;top:272px}
.arrow.prev{left:10px}.arrow.next{right:10px}

/* Intro */
.intro{top:588px;height:652px;background:var(--bg);text-align:center}
.intro h2{position:absolute;width:100%;font-family:"Cabin",Helvetica,sans-serif;font-weight:500;font-size:29px;color:var(--ink)}
.intro p{position:absolute;left:168px;width:864px;font-size:15px;line-height:27px;color:var(--text)}
.intro .btn{left:505px;top:565px;width:172px;height:46px;line-height:46px}

/* Image bands */
.band{display:flex;flex-direction:column;align-items:center;justify-content:center;color:var(--white);font-family:"Cabin",Helvetica,sans-serif;font-weight:600;text-transform:uppercase;text-shadow:0 2px 6px rgba(0,0,0,.55)}
.band-services{top:1240px;height:393px;background:linear-gradient(180deg,#5c6a88 0%,#8191ac 30%,#4a4f63 58%,#2e3547 72%,#4c6a92 86%,#2d4565 100%);font-size:42px;line-height:62px;text-align:center}
.band-news{top:1922px;height:395px;background:linear-gradient(90deg,#b9a78c 0%,#e3ded6 30%,#cfcac2 55%,#e6e5e1 75%,#a9a59e 100%);font-size:42px}

/* Services */
.services{top:1633px;height:289px;background:var(--bg)}
.service{position:absolute;top:34px}
.service h3{font-family:"Cabin",Helvetica,sans-serif;font-weight:500;font-size:25px;color:var(--ink);margin-bottom:18px}
.service li{list-style:none;font-size:15px;font-weight:700;color:var(--ink);line-height:32px}
.more{font-family:"Cabin",Helvetica,sans-serif;font-weight:600;font-size:19px;color:var(--link);display:block}
.service .more{margin-top:10px}

/* News & events */
.feed{top:2317px;height:443px;background:var(--bg)}
.feed-col{position:absolute;top:36px}
.feed-col h3{font-family:"Cabin",Helvetica,sans-serif;font-weight:500;font-size:25px;color:var(--ink);margin-bottom:20px}
.item{display:flex;gap:22px;height:112px;margin-bottom:36px}
.thumb{width:211px;height:112px;flex:none}
.item h4{font-family:"Cabin",Helvetica,sans-serif;font-weight:500;font-size:20px;color:var(--ink);margin-top:10px}
.item time{display:block;font-size:18px;color:var(--muted);margin-top:8px}
.feed-col .more{margin-top:-8px}

/* Footer */
.subscribe{top:2760px;height:395px;background:var(--footer);text-align:center}
.social{position:absolute;top:2px;left:529px;display:flex;gap:9px;margin-top:42px}
.social span{width:36px;height:36px;border-radius:50%;background:var(--white);display:block}
.subscribe h3{position:absolute;top:134px;width:100%;font-family:"Lato",Helvetica,sans-serif;font-weight:300;font-size:27px;letter-spacing:1px;color:#e6e6e6}
.signup{position:absolute;left:402px;top:203px;display:flex;gap:9px}
.signup .field{width:239px;height:47px;background:var(--white);font-family:Georgia,serif;font-size:12px;color:#aaa;text-align:left;padding:16px 12px}
.signup .send{width:130px;height:47px;background:#565656;color:var(--white);font-family:Georgia,serif;font-size:13px;line-height:47px;text-transform:uppercase}
.search{position:absolute;left:244px;top:308px;width:699px;height:43px;border:3px solid #d8d8d8;border-radius:5px;display:flex;align-items:center;gap:12px;padding-left:14px;color:#e6e6e6;font-size:15px}
.contact{top:3155px;height:197px;background:var(--footer-deep);text-align:center;color:#e0e0e0}
.contact h3{margin-top:40px;font-family:Helvetica,Arial,sans-serif;font-weight:700;font-size:25px;letter-spacing:1px}
.contact p{margin-top:20px;font-family:Helvetica,Arial,sans-serif;font-size:17px;letter-spacing:1px;line-height:33px;text-transform:uppercase}
</style>
</head>
<body>

<header class="hero" role="img" aria-label="Harbour with moored boats in front of a hillside town">
  <div class="brand">
    <span class="brand-mark"></span>
    <span class="brand-name">BRENMOOR ESTATES LTD</span>
  </div>
  <nav class="main-nav"><span>Home</span><span>About</span><span>News</span><span>Events</span><span>Blog</span><span>Contact</span></nav>
  <span class="cta">GET STARTED</span>
  <svg class="arrow prev" width="30" height="36" viewBox="0 0 30 36"><path d="M22 4 8 18l14 14" fill="none" stroke="#fff" stroke-width="6"/></svg>
  <svg class="arrow next" width="30" height="36" viewBox="0 0 30 36"><path d="M8 4l14 14L8 32" fill="none" stroke="#fff" stroke-width="6"/></svg>
  <p class="hero-kicker">Lorem Ipsum is simply dummy text</p>
  <h1 class="hero-title">Brenmoor Estates Limited</h1>
  <span class="btn">LEARN MORE</span>
</header>

<section class="intro">
  <h2 style="top:50px">Brenmoor Estates Limited</h2>
  <p style="top:103px">Brenmoor Estates Limited (BEL) is a family-owned Guernsey property holding company. It purchases properties that are considered to have potential for development either through refurbishment or by obtaining planning permission to change its classification from, for example, industrial premises to offices or retail outlets, or by the marriage value of buying an adjacent property to one already owned by BEL.</p>
  <p style="top:256px">BEL's reputation as a fair-minded landlord stems from the application of the founder's tenet of working with the tenant to help maximise the business benefits of both parties. There is no capital gains tax on the sale of property in the Island which makes buying and selling an attractive enterprise.</p>
  <h2 style="top:378px">Why Guernsey?</h2>
  <p style="top:430px">The Bailiwick of Guernsey is a British Crown dependency in the English Channel. The benefit of establishing a company in Guernsey is the island's low tax jurisdiction since there are no capital taxes and no corporation taxes for many companies. Consequently since the 1980s the island's development as an ideal financial centre for the establishment of institutions and banks has thrived.</p>
  <span class="btn">LEARN MORE</span>
</section>

<section class="band band-services" role="img" aria-label="City skyline at dusk across the water">
  <span>Why</span><span>Property Management Services</span>
</section>

<section class="services">
  <div class="service" style="left:176px">
    <h3>For Property Owners</h3>
    <ul><li>Lorem ipsum dolor sit</li><li>Lorem ipsum dolor sit</li><li>Lorem ipsum dolor sit</li><li>Lorem ipsum dolor sit</li></ul>
    <span class="more">Read more.</span>
  </div>
  <div class="service" style="left:476px">
    <h3>For Property Owners</h3>
    <ul><li>Lorem ipsum dolor sit</li><li>Lorem ipsum dolor sit</li><li>Lorem ipsum dolor sit</li><li>Lorem ipsum dolor sit</li></ul>
    <span class="more">Read more.</span>
  </div>
  <div class="service" style="left:773px">
    <h3>For Property Owners</h3>
    <ul><li>Lorem ipsum dolor sit</li><li>Lorem ipsum dolor sit</li><li>Lorem ipsum dolor sit</li><li>Lorem ipsum dolor sit</li></ul>
    <span class="more">Read more.</span>
  </div>
</section>

<section class="band band-news" role="img" aria-label="Bright modern living room interior">
  <span>News &amp; Events</span>
</section>

<section class="feed">
  <div class="feed-col" style="left:176px">
    <h3>Upcoming Events</h3>
    <div class="item">
      <div class="thumb" role="img" aria-label="Audience at an event" style="background:linear-gradient(135deg,#7b5b57,#c9a79a 50%,#5a4a5a)"></div>
      <div><h4>Lorem Ipsum</h4><time>Dec 3, 2016</time></div>
    </div>
    <div class="item">
      <div class="thumb" role="img" aria-label="Sunlit room with wooden floor" style="background:linear-gradient(135deg,#a58462,#e2d4bd 50%,#8b6a4b)"></div>
      <div><h4>Lorem Ipsum</h4><time>Dec 3, 2016</time></div>
    </div>
    <span class="more">Load more.</span>
  </div>
  <div class="feed-col" style="left:628px">
    <h3>Latest News</h3>
    <div class="item">
      <div class="thumb" role="img" aria-label="Meeting in an office" style="background:linear-gradient(135deg,#cfcdc6,#8d8a84 55%,#55524f)"></div>
      <div><h4>Lorem Ipsum</h4><time>Dec 3, 2016</time></div>
    </div>
    <div class="item">
      <div class="thumb" role="img" aria-label="Modern apartment building" style="background:linear-gradient(180deg,#6f9ad4,#b56d4a 50%,#6f6b62)"></div>
      <div><h4>Lorem Ipsum</h4><time>Dec 3, 2016</time></div>
    </div>
    <span class="more">Load more.</span>
  </div>
</section>

<footer class="subscribe">
  <div class="social" aria-label="Social links"><span></span><span></span><span></span></div>
  <h3>Subscribe to our eBulletin</h3>
  <div class="signup"><span class="field">Email Address</span><span class="send">Sign up</span></div>
  <div class="search">
    <svg width="24" height="24" viewBox="0 0 24 24"><circle cx="14" cy="9" r="7" fill="none" stroke="#111" stroke-width="3"/><path d="M9 14 2 21" stroke="#111" stroke-width="4"/></svg>
    <span>Search</span>
  </div>
</footer>

<footer class="contact">
  <h3>CONTACT US</h3>
  <p>Brenmoor Estates Ltd, Your Street, Your Country, Your State,<br>Kingdom &nbsp;(012) 3456 7890 &nbsp;info@brenmoorestates.example</p>
</footer>

</body>
</html>
```